Velmora Partners - website for real estate investment company

Create a bold, modern website that reflects Velmora’s success, professionalism, and credibility.
The design must stand out while maintaining a polished, corporate tone. (bold, but understated)
The client just created a new logo, and the website design must be in sync with the logo design. Information about the logo colors, fonts, and message are in the attached design brief.
Updates

Target Market(s)

b2b: banks, brokers, institutional partners, vendors, and property sellers.

Industry/Entity Type

real estate investment company

Number of Pages Required

1 page

Font styles to use
Sans Serif

Colors

Designer to choose colors to be used in the design.

Requirements
Must have
• 1. homepage design (psd) 2. a top banner image (psd) for a default inner page
Nice to have
• please see attached design brief
Should not have

```html
<!DOCTYPE html>
<html lang="en">
<head>
<meta charset="utf-8">
<title>Velmora Partners – Real Estate Investment</title>
<link href="https://fonts.googleapis.com/css2?family=Oswald:wght@500;600;700&family=Montserrat:wght@400;500;600;700&display=swap" rel="stylesheet">
<style>
:root{
  --red:#e1232a;
  --red-dark:#b81b21;
  --ink:#1b1b1b;
  --panel:#222222;
  --panel-2:#2a2a2a;
  --white:#ffffff;
  --muted:#cfcfcf;
  --line:#5a5a5a;
  --head:'Oswald',sans-serif;
  --body:'Montserrat',sans-serif;
}
*{box-sizing:border-box;margin:0;padding:0}
html,body{width:1200px;height:4501px;overflow:hidden}
body{position:relative;background:var(--ink);color:var(--white);font-family:var(--body)}
.abs{position:absolute}
h1,h2,h3,h4{font-family:var(--head);font-weight:600;text-transform:uppercase}
a{color:inherit;text-decoration:none}
.btn{position:absolute;display:inline-flex;align-items:center;justify-content:center;font-size:11px;font-weight:500;height:30px;padding:0 24px;overflow:hidden}
.btn::after{content:"";position:absolute;right:0;bottom:0;border-style:solid;border-width:0 0 14px 14px;border-color:transparent transparent var(--white) transparent}
.btn-red{background:var(--red);color:var(--white)}
.btn-white{background:var(--white);color:var(--red)}
.btn-white::after{border-color:transparent transparent var(--red) transparent}
.photo{position:absolute}
.section-title{display:flex;align-items:center;gap:20px;font-size:40px;letter-spacing:.5px}
.section-title .rule{height:2px;width:85px;background:var(--red)}
.section-title .rule.w{background:var(--white)}

/* nav */
.nav{top:0;left:0;width:1200px;height:65px;background:#1a1a1a;display:flex;align-items:center}
.brand{font-family:var(--head);font-weight:700;font-size:30px;color:var(--white);letter-spacing:1px}
.nav .brand{position:absolute;left:100px;top:13px}
.nav-links{position:absolute;left:300px;top:26px;display:flex;gap:32px;font-size:11px}
.nav-links .active{color:var(--red)}
.nav-phone{position:absolute;left:840px;top:25px;font-size:11px;font-weight:600;display:flex;gap:8px;align-items:center}
.nav .btn{left:988px;top:18px;width:112px}

/* hero */
.hero{top:65px;left:0;width:1200px;height:550px;overflow:hidden}
.hero .photo{inset:0;background:linear-gradient(180deg,#e99a6a 0%,#b9878a 28%,#6f7488 55%,#3e4552 100%)}
.hero .shade{position:absolute;inset:0;background:linear-gradient(90deg,rgba(20,20,20,.75) 0%,rgba(20,20,20,.35) 45%,rgba(0,0,0,0) 70%)}
.hero-title{position:absolute;left:100px;top:76px;font-size:57px;font-weight:700;letter-spacing:.5px}
.hero-title .line{display:block;height:65px;line-height:65px;white-space:nowrap}
.hero-title .mark{display:inline-block;height:58px;line-height:58px;background:var(--white);color:var(--red);padding:0 6px;margin-left:-6px;vertical-align:top;margin-top:4px}
.hero p{position:absolute;left:100px;top:355px;width:390px;font-size:10.5px;line-height:17px}
.hero .btn{left:100px;top:443px}

/* stats */
.stats{top:615px;left:0;width:1200px;height:197px;background:var(--panel)}
.stat{position:absolute;top:55px;width:330px;text-align:center}
.stat .num{font-family:var(--head);font-size:40px;color:var(--red);font-weight:500}
.stat .lbl{font-size:14px;margin-top:8px}
.divider{position:absolute;top:44px;width:2px;height:110px;background:#777}

/* about */
.about{top:812px;left:0;width:1200px;height:498px;overflow:hidden}
.about .frame-a{left:100px;top:10px;width:130px;height:130px;border-top:10px solid var(--red);border-left:10px solid var(--red)}
.about .frame-b{left:515px;top:285px;width:130px;height:130px;border-bottom:10px solid var(--red);border-right:10px solid var(--red)}
.about .photo{left:108px;top:20px;width:530px;height:392px;background:linear-gradient(160deg,#bfc3c8 0%,#9aa0a7 45%,#6d747c 100%)}
.about h2{position:absolute;left:683px;top:30px}
.about .copy{position:absolute;left:683px;top:95px;width:415px;font-size:11.5px;line-height:18.8px}
.about .copy p+p{margin-top:9px}
.about .btn{left:683px;top:358px}
.about .ghost{position:absolute;left:1128px;top:362px;transform:rotate(-90deg);transform-origin:left top;font-family:var(--head);font-weight:700;font-size:80px;line-height:80px;color:#3a3a3a;white-space:nowrap}

/* portfolio */
.portfolio{top:1310px;left:0;width:1200px;height:480px}
.portfolio .band{left:0;top:0;width:740px;height:330px;background:linear-gradient(90deg,#3a3a3a,#2c2c2c)}
.portfolio .arrows{left:625px;top:0;width:118px;height:85px;background:var(--red)}
.arrow-btn{position:absolute;top:25px;width:32px;height:28px;background:var(--white);display:flex;align-items:center;justify-content:center}
.portfolio h2{position:absolute;left:100px;top:65px}
.portfolio p{position:absolute;left:100px;top:135px;width:350px;font-size:11.5px;line-height:19px}
.portfolio .btn{left:100px;top:218px;width:145px}
.card{position:absolute;top:88px;width:256px}
.card .photo{position:relative;width:256px;height:300px}
.card h4{font-size:14px;font-weight:500;margin-top:16px}
.card .loc{font-family:var(--head);font-size:14px;font-weight:500;margin-top:4px}

/* approach */
.approach{top:1800px;left:0;width:1200px;height:400px}
.approach .section-title{position:absolute;left:0;width:1200px;top:20px;justify-content:center}
.step{position:absolute;top:105px;width:280px;text-align:center}
.step svg{display:block;margin:0 auto}
.step h4{font-size:14px;font-weight:500;margin-top:18px}
.step p{font-size:11.5px;line-height:18.5px;margin-top:12px}
.approach .btn{left:480px;top:308px;width:240px}

/* features */
.features{top:2210px;left:0;width:1200px;height:506px}
.feature{position:absolute;top:0;width:400px;height:506px;overflow:hidden}
.feature .photo{inset:0}
.feature .overlay{position:absolute;inset:0;background:linear-gradient(180deg,rgba(0,0,0,0) 45%,rgba(15,15,15,.85) 100%)}
.feature .txt{position:absolute;left:0;right:0;top:400px;text-align:center}
.feature h4{font-size:14px;font-weight:500}
.feature p{font-size:11.5px;line-height:18.5px;margin:10px auto 0;width:300px}
.feature .bar{width:85px;height:2px;background:var(--red);margin:9px auto 0}

/* partners */
.partners{top:2786px;left:97px;width:1006px;height:88px;display:flex;justify-content:space-between}
.badge{width:88px;height:88px;background:var(--white);display:flex;align-items:center;justify-content:center}
.badge span{width:52px;height:52px;background:#8a8a8a;border-radius:50%}

/* news */
.news{top:2934px;left:0;width:1200px;height:700px}
.news .section-title{position:absolute;left:0;width:1200px;top:0;justify-content:center}
.date{font-size:10px;color:var(--red)}
.lead{position:absolute;left:100px;top:100px;width:400px}
.lead h3{color:var(--red);font-size:25px;line-height:33px;font-weight:600;margin-top:12px}
.lead p{font-size:11.5px;line-height:18.5px;margin-top:10px;width:320px}
.more{display:inline-block;font-size:10px;color:var(--red);text-decoration:underline;margin-top:18px}
.news .frame-a{left:578px;top:160px;width:120px;height:190px;border-left:8px solid var(--red);border-bottom:8px solid var(--red);clip-path:polygon(0 25%,100% 100%,0 100%)}
.news .frame-b{left:960px;top:96px;width:125px;height:150px;border-top:8px solid var(--red);border-right:8px solid var(--red);clip-path:polygon(0 0,100% 0,100% 75%)}
.news .lead-photo{left:587px;top:102px;width:490px;height:305px;background:linear-gradient(150deg,#f2efea 0%,#d9d3cb 50%,#b4a89a 100%)}
.mini{position:absolute;top:475px;width:285px}
.mini h4{font-size:14px;line-height:22px;font-weight:500;margin-top:10px}
.mini .more{margin-top:6px}
.mini-photo{position:absolute;top:478px;width:174px;height:125px}
.news .btn{left:523px;top:643px;width:154px}

/* contact */
.contact{top:3677px;left:0;width:1200px;height:550px;overflow:hidden;background:linear-gradient(180deg,#2a2a2a 0%,#262a30 55%,#1e1f22 100%)}
.contact .tri{right:0;top:0;width:280px;height:230px;background:var(--red);clip-path:polygon(0 0,100% 0,100% 100%)}
.form{position:absolute;left:100px;top:75px;width:470px;height:458px;background:var(--red);padding:35px 38px}
.form h2{font-size:40px;font-weight:500}
.field{background:var(--white);height:32px;margin-top:14px;font-size:10px;color:#8a8a8a;padding:9px 12px}
.field:first-of-type{margin-top:22px}
.field.area{height:74px}
.form .btn{position:relative;margin-top:32px;width:112px;background:var(--white);color:var(--red)}
.form .btn::after{border-color:transparent transparent var(--red) transparent}
.contact .brand{position:absolute;left:750px;top:110px;font-size:46px}
.info{position:absolute;left:750px;display:flex;gap:16px}
.info .ico{width:30px;height:30px;border-radius:50%;background:var(--red);display:flex;align-items:center;justify-content:center;flex:none}
.info h4{font-size:16px;font-weight:500}
.info .big{font-family:var(--head);font-size:18px;font-weight:500;margin-top:4px}
.info .small{font-size:12px;line-height:17px;margin-top:4px}

/* footer */
.footer{top:4227px;left:0;width:1200px;height:274px;background:#1b1b1b}
.footer .brand{position:absolute;left:100px;top:25px;font-size:70px}
.socials{position:absolute;left:145px;top:130px;display:flex;gap:12px}
.socials span{width:30px;height:30px;border:1.5px solid var(--white);border-radius:50%}
.col{position:absolute;top:26px}
.col h4{font-size:14px;font-weight:500}
.col ul{list-style:none;font-size:11px;line-height:22.5px;margin-top:12px}
.sub-field{width:256px;height:32px;border:1px solid #888;font-size:9px;padding:10px 12px;margin-top:16px}
.sub-btn{position:relative;width:256px;height:30px;background:var(--red);font-size:11px;display:flex;align-items:center;justify-content:center;margin-top:12px;overflow:hidden}
.sub-btn::after{content:"";position:absolute;right:0;bottom:0;border-style:solid;border-width:0 0 14px 14px;border-color:transparent transparent var(--white) transparent}
.footer .rule{left:100px;top:228px;width:1000px;height:1px;background:#555}
.copyright{position:absolute;left:0;width:1200px;top:243px;text-align:center;font-size:10px}
</style>
</head>
<body>

<header class="nav abs">
  <a class="brand" href="#">VELMORA</a>
  <nav class="nav-links">
    <a class="active" href="#">Home</a><a href="#">Our Story</a><a href="#">Investment Strategy</a><a href="#">What Sets Us Apart</a><a href="#">Our Portfolio</a>
  </nav>
  <div class="nav-phone">
    <svg width="13" height="13" viewBox="0 0 24 24" fill="none" stroke="#fff" stroke-width="2.4"><circle cx="10" cy="10" r="7"/><path d="M15 15l6 6"/></svg>
    <span style="width:10px"></span>
    <svg width="12" height="12" viewBox="0 0 24 24" fill="#fff"><path d="M6.6 10.8a15 15 0 006.6 6.6l2.2-2.2a1 1 0 011-.25 11.4 11.4 0 003.6.6 1 1 0 011 1V20a1 1 0 01-1 1A17 17 0 013 4a1 1 0 011-1h3.5a1 1 0 011 1 11.4 11.4 0 00.6 3.6 1 1 0 01-.25 1z"/></svg>
    (555) 014-2260
  </div>
  <a class="btn btn-red" href="#">Contact Us</a>
</header>

<section class="hero abs">
  <div class="photo" role="img" aria-label="City skyline at sunset with high-rise towers"></div>
  <div class="shade"></div>
  <svg class="abs" style="left:0;top:0" width="270" height="230"><polygon points="0,0 270,0 0,230" fill="#e1232a" opacity=".85"/></svg>
  <h1 class="hero-title">
    <span class="line">Investing in</span>
    <span class="line"><span class="mark">Communities.</span></span>
    <span class="line">Delivering</span>
    <span class="line"><span class="mark">Lasting Value.</span></span>
  </h1>
  <p>Velmora Partners is a vertically integrated real estate investment firm with a proven four-decade track record. We acquire, reposition, and operate high-performing assets across multiple sectors — always with a focus on exceptional, risk-adjusted returns.</p>
  <a class="btn btn-white" href="#">Explore Our Portfolio</a>
</section>

<section class="stats abs">
  <div class="stat" style="left:127px"><div class="num">FOUNDED 1989</div><div class="lbl">Years of experience</div></div>
  <div class="divider" style="left:465px"></div>
  <div class="stat" style="left:475px"><div class="num">23,000+</div><div class="lbl">Multifamily &amp; healthcare units</div></div>
  <div class="divider" style="left:797px"></div>
  <div class="stat" style="left:772px"><div class="num">$300M+</div><div class="lbl">Invested in renovations</div></div>
</section>

<section class="about abs">
  <div class="abs frame-a"></div>
  <div class="abs frame-b"></div>
  <div class="photo" role="img" aria-label="Team meeting around a table with an architectural building model"></div>
  <div class="ghost">VELMORA</div>
  <h2 class="section-title">About Us <span class="rule"></span></h2>
  <div class="copy">
    <p>Founded in <b>1989</b>, Velmora Partners is a privately held real estate investment firm specializing in the acquisition, development, and management of multifamily and healthcare properties. With a portfolio spanning <b>23,000+ units</b> and over <b>$300 million</b> invested in renovations, we deliver sustainable growth and superior returns through strategic acquisitions, hands-on asset management, and value-driven improvements.</p>
    <p>Our experienced team combines market insight with operational expertise to identify opportunities, enhance property performance, and strengthen communities. Built on integrity, vision, and results, Velmora Partners continues to lead with a proven track record of success across diverse real estate markets.</p>
  </div>
  <a class="btn btn-white" href="#">Read More</a>
</section>

<section class="portfolio abs">
  <div class="abs band"></div>
  <div class="abs arrows">
    <span class="arrow-btn" style="left:18px"><svg width="10" height="10" viewBox="0 0 10 10"><path d="M7 1L3 5l4 4" stroke="#e1232a" stroke-width="2" fill="none"/></svg></span>
    <span class="arrow-btn" style="left:58px"><svg width="10" height="10" viewBox="0 0 10 10"><path d="M3 1l4 4-4 4" stroke="#e1232a" stroke-width="2" fill="none"/></svg></span>
  </div>
  <h2 class="section-title">Our Portfolio <span class="rule w"></span></h2>
  <p>Our experienced team combines market insight with operational expertise to identify opportunities, enhance property performance, and strengthen communities</p>
  <a class="btn btn-white" href="#">View More</a>
  <div class="card" style="left:520px">
    <div class="photo" role="img" aria-label="Waterfront residential building with red roofs" style="background:linear-gradient(180deg,#e8eef4 0%,#c9c6c0 55%,#3aa6b5 85%,#2b8fa0 100%)"></div>
    <h4>Riverview Care Center</h4><div class="loc">— TRENTON, NJ</div>
  </div>
  <div class="card" style="left:788px">
    <div class="photo" role="img" aria-label="Glass residential towers" style="background:linear-gradient(180deg,#c9d3dc 0%,#7d8891 50%,#4c5660 100%)"></div>
    <h4>Harbor Point Residences</h4><div class="loc">— PHILADELPHIA, PA</div>
  </div>
  <div class="card" style="left:1056px">
    <div class="photo" role="img" aria-label="Apartment towers behind autumn trees" style="background:linear-gradient(180deg,#5d8fd0 0%,#b49a7a 50%,#6a7a3a 100%)"></div>
    <h4 style="white-space:nowrap">Maple Grove Apartments</h4><div class="loc">— BALTIMORE, MD</div>
  </div>
</section>

<section class="approach abs">
  <h2 class="section-title"><span class="rule"></span>Our Investment Approach<span class="rule"></span></h2>
  <div class="step" style="left:122px">
    <svg width="66" height="66" viewBox="0 0 66 66"><path d="M8 6h30l10 10v44H8z" fill="#e1232a"/><rect x="15" y="20" width="18" height="3" fill="#1b1b1b"/><rect x="15" y="28" width="14" height="3" fill="#1b1b1b"/><circle cx="42" cy="42" r="11" fill="#1b1b1b" stroke="#e1232a" stroke-width="4"/><path d="M50 50l10 10" stroke="#e1232a" stroke-width="5"/></svg>
    <h4>Identify Opportunities</h4>
    <p>Pinpoint high-potential assets through data-driven research and decades of industry expertise.</p>
  </div>
  <div class="step" style="left:460px">
    <svg width="66" height="66" viewBox="0 0 66 66"><path d="M33 4l24 20h-7v36H16V24H9z" fill="#e1232a"/><text x="33" y="50" text-anchor="middle" font-family="Montserrat" font-weight="700" font-size="18" fill="#1b1b1b">$</text><path d="M50 4v14M44 9l6-6 6 6" stroke="#e1232a" stroke-width="3" fill="none"/></svg>
    <h4>Maximize Value</h4>
    <p>Execute targeted renovations and operational enhancements that boost performance and returns.</p>
  </div>
  <div class="step" style="left:798px">
    <svg width="66" height="66" viewBox="0 0 66 66"><circle cx="20" cy="12" r="6" fill="#e1232a"/><circle cx="33" cy="9" r="6" fill="#e1232a"/><circle cx="46" cy="12" r="6" fill="#e1232a"/><path d="M10 30c0-8 20-8 20 0M23 27c0-8 20-8 20 0M36 30c0-8 20-8 20 0" fill="#e1232a"/><path d="M6 40l14-6 13 8 13-8 14 6-14 18H20z" fill="#e1232a"/></svg>
    <h4>Strengthen Communities</h4>
    <p>Foster vibrant, sustainable communities through quality improvements and responsible management.</p>
  </div>
  <a class="btn btn-white" href="#">Learn More About Our Approach</a>
</section>

<section class="features abs">
  <div class="feature" style="left:0">
    <div class="photo" role="img" aria-label="Financial bar chart on a desk with a laptop" style="background:linear-gradient(160deg,#7a6a5a 0%,#9fb0bd 45%,#3b8fb0 100%)"></div>
    <div class="overlay"></div>
    <div class="txt"><h4>Proven Track Record</h4><p>35+ years of success managing diverse real estate assets across the U.S.</p><div class="bar"></div></div>
  </div>
  <div class="feature" style="left:401px">
    <div class="photo" role="img" aria-label="Business professionals shaking hands in an office" style="background:linear-gradient(160deg,#d8d8d8 0%,#9a9a9a 50%,#4a4a4a 100%)"></div>
    <div class="overlay"></div>
    <div class="txt"><h4>Hands-On Management</h4><p>Active oversight ensures every property meets our high performance and quality.</p><div class="bar"></div></div>
  </div>
  <div class="feature" style="left:802px">
    <div class="photo" role="img" aria-label="Aerial view of a dense residential neighborhood" style="background:linear-gradient(180deg,#b9c4cc 0%,#8b959c 45%,#4f5a60 100%)"></div>
    <div class="overlay"></div>
    <div class="txt"><h4>Commitment to Communities</h4><p>We invest in ways that improve lives, strengthen neighborhoods.</p><div class="bar"></div></div>
  </div>
</section>

<div class="partners abs" aria-label="Partner badges">
  <div class="badge"><span></span></div><div class="badge"><span></span></div><div class="badge"><span></span></div><div class="badge"><span></span></div><div class="badge"><span></span></div><div class="badge"><span></span></div><div class="badge"><span></span></div>
</div>

<section class="news abs">
  <h2 class="section-title"><span class="rule"></span>Our Latest News<span class="rule"></span></h2>
  <article class="lead">
    <div class="date">25 June, 2025</div>
    <h3>Mid-Year Outlook: Global Shocks Provide Generational Opportunity for Those Who Know Where to Look</h3>
    <p>Our experienced team combines market insight with operational expertise to identify opportunities, enhance property performance, and strengthen communities. Built on integrity,</p>
    <a class="more" href="#">Learn More</a>
  </article>
  <div class="abs frame-a"></div>
  <div class="abs frame-b"></div>
  <div class="photo lead-photo" role="img" aria-label="Couple reviewing building plans in a bright room"></div>

  <article class="mini" style="left:100px">
    <div class="date">25 June, 2025</div>
    <h4>Lorem Ipsum has been the industry's standard dummy text ever since the 1500s, type and scrambled it to specimen book.</h4>
    <a class="more" href="#">Learn More</a>
  </article>
  <div class="photo mini-photo" style="left:418px;background:linear-gradient(150deg,#f0ede8,#c9beb2)" role="img" aria-label="Hand signing a property document beside a house model"></div>
  <article class="mini" style="left:611px">
    <div class="date">25 June, 2025</div>
    <h4>Lorem Ipsum has been the industry's standard dummy text ever since the 1500s, type and scrambled it to specimen book.</h4>
    <a class="more" href="#">Learn More</a>
  </article>
  <div class="photo mini-photo" style="left:926px;background:linear-gradient(180deg,#8fb0cf,#6c8a6a)" role="img" aria-label="Aerial city skyline with green park"></div>
  <a class="btn btn-white" href="#">View More News</a>
</section>

<section class="contact abs">
  <div class="abs tri"></div>
  <form class="form">
    <h2>Get In Touch</h2>
    <div class="field">Name</div>
    <div class="field">Email</div>
    <div class="field">Phone</div>
    <div class="field">Select Service</div>
    <div class="field area">Messages</div>
    <span class="btn">Submit</span>
  </form>
  <div class="brand">VELMORA</div>
  <div class="info" style="top:193px">
    <span class="ico"><svg width="14" height="14" viewBox="0 0 24 24" fill="#fff"><path d="M6.6 10.8a15 15 0 006.6 6.6l2.2-2.2a1 1 0 011-.25 11.4 11.4 0 003.6.6 1 1 0 011 1V20a1 1 0 01-1 1A17 17 0 013 4a1 1 0 011-1h3.5a1 1 0 011 1 11.4 11.4 0 00.6 3.6 1 1 0 01-.25 1z"/></svg></span>
    <div><h4>Call Now</h4><div class="big">(555) 014-2260</div></div>
  </div>
  <div class="info" style="top:264px">
    <span class="ico"><svg width="14" height="14" viewBox="0 0 24 24" fill="none" stroke="#fff" stroke-width="2.2"><rect x="3" y="5" width="18" height="14"/><path d="M3 6l9 7 9-7"/></svg></span>
    <div><h4>Email Now</h4><div class="small">info@velmora.com</div></div>
  </div>
  <div class="info" style="top:322px">
    <span class="ico"><svg width="14" height="14" viewBox="0 0 24 24" fill="#fff"><path d="M12 2a7 7 0 00-7 7c0 5 7 13 7 13s7-8 7-13a7 7 0 00-7-7zm0 9.5A2.5 2.5 0 1112 6.5a2.5 2.5 0 010 5z"/></svg></span>
    <div><h4>Address</h4><div class="small">420 Harbor Ave, Lakeview,<br>NJ 08000</div></div>
  </div>
</section>

<footer class="footer abs">
  <div class="brand">VELMORA</div>
  <div class="socials"><span></span><span></span><span></span><span></span></div>
  <div class="col" style="left:533px">
    <h4>Quick Links</h4>
    <ul><li>Home</li><li>Our Story</li><li>Investment Strategy</li><li>What Sets Us Apart</li><li>Our Portfolio</li><li>Contact Us</li></ul>
  </div>
  <div class="col" style="left:845px">
    <h4>Subscribe Newsletter</h4>
    <div class="sub-field">Email</div>
    <div class="sub-btn">Subscribe Now</div>
  </div>
  <div class="abs rule"></div>
  <div class="copyright">© Copyright All Right Reserved 2025</div>
</footer>

</body>
</html>
```